Redesign of TaskHarbor.com website

Our website was initially developed 6+ years ago and has been maintained by several different designers. As a result, it is overly complex, inconsistent format/layout and the content is not well structured/easy to navigate

We need the site redeveloped with a more modern look and feel, simpler content structure and ability to implement new/improved tools, such as: Dynamic Forms, Sales Funnels, Landing Pages, improved metadata of our pages and posts, improved SEO/Page ranking, etc.

We currently use DealRiver CRM, Steady Reach for marketing automation and GridPilot forms. We are investigating Floxen for workflow integration which could extend to our website.

Our current website is developed in WordPress, ideally we will stick with this platform, but we’re happy to consider other CMS' if strongly recommended. We may decide to remove/consolidate some of the pages and/or content as part of this re-design.

We don't want to rebrand (ie change corporate logo, colours scheme etc) as part of this website redevelopment and it is critical that we don't lose our current Page Ranking, SEO rankings, backlink benefits, etc as part of this redevelopment.

Sites we like the feel/design of are: boardwiley.com, tallypoint.com and rankgrove.com

Target Market(s)

Corporate, Enterprise and Government B2B clients.

Coding

Coded - Design and coding required

Number of Pages Required

5+ page

Font styles to use
Sans Serif

Colors
ffffff
ec1f27

Requirements
Must have
• Must retain the majority of content on our existing website (although we may re-write some of it as part of this redesign process).
Nice to have
• See above "Project Description"
Should not have

```html
<!DOCTYPE html>
<html lang="en">
<head>
<meta charset="utf-8">
<title>TaskHarbor – Your Trusted Advisor For Business Continuity Solutions</title>
<link href="https://fonts.googleapis.com/css2?family=Lato:wght@300;400;700;900&display=swap" rel="stylesheet">
<style>
:root{
  --brand:#ec1f27;
  --accent:#d2453e;
  --ink:#2e2e2e;
  --text:#555;
  --muted:#777;
  --hero-bg:#f4f4f4;
  --band:#f2f2f2;
  --line:#e3e3e3;
  --white:#ffffff;
  --footer:#2d2d2d;
  --footer-text:#cfcfcf;
}
*{box-sizing:border-box;margin:0;padding:0}
html,body{width:1200px;height:4525px;overflow:hidden}
body{font-family:'Lato',sans-serif;color:var(--text);background:var(--white);position:relative}
.abs{position:absolute}
a{color:inherit;text-decoration:none}
.btn{position:absolute;display:inline-flex;align-items:center;justify-content:center;background:var(--accent);color:var(--white);font-weight:700;font-size:16px;border-radius:30px;text-transform:uppercase;letter-spacing:.2px}
.placeholder{position:absolute}
.card{position:absolute;background:var(--white);border-radius:12px;box-shadow:0 4px 22px rgba(0,0,0,.08)}

/* header + hero */
.hero{position:absolute;left:0;top:0;width:1200px;height:738px;background:var(--hero-bg)}
.logo{position:absolute;display:flex;align-items:center;gap:10px}
.logo-dot{width:36px;height:36px;border-radius:50%;background:var(--brand)}
.logo-name{font-size:34px;font-weight:400;color:var(--brand);letter-spacing:-.5px;line-height:1}
.logo-tag{font-size:11px;color:var(--muted);text-align:right;margin-top:-2px}
.nav{position:absolute;left:401px;top:48px;display:flex;gap:24px;font-size:17px;color:var(--ink)}
.nav .active{color:var(--brand)}
.phone{position:absolute;left:934px;top:48px;font-size:18px;color:#555;display:flex;align-items:center;gap:7px}
.hero h1{position:absolute;left:110px;top:196px;font-size:74px;font-weight:700;color:var(--ink);letter-spacing:-.5px}
.hero .lead{position:absolute;left:112px;top:298px;font-size:21px;line-height:31px;color:#555;width:380px}

/* trusted */
.trusted-title{position:absolute;left:0;width:1200px;top:694px;text-align:center;font-size:40px;font-weight:700;color:var(--ink)}
.client{position:absolute;top:769px;width:170px;height:94px;border:1px solid #ddd;display:flex;align-items:center;justify-content:center;font-size:26px;font-weight:700;color:#aaa;background:var(--white)}
.client.active{border-color:var(--accent);color:var(--accent);font-size:22px}
.arrow{position:absolute;top:808px;width:20px;height:20px}

/* welcome */
h2{font-weight:700;color:var(--ink)}
.welcome h2{position:absolute;left:110px;top:958px;font-size:42px}
.body-copy{font-size:15.5px;line-height:26px;color:#666}
.ticks{list-style:none}
.ticks li{display:flex;align-items:center;gap:10px;font-size:15.5px;color:#666;line-height:27px}
.tick{width:14px;height:14px;flex:none}

/* what we do */
.band{position:absolute;left:0;width:1200px;background:var(--band)}
.section-title{position:absolute;left:0;width:1200px;text-align:center;font-size:42px;font-weight:700;color:var(--ink)}
.tab{position:absolute;top:1580px;width:164px;text-align:center;font-size:20px;line-height:26px;color:#444}
.tab .icon{width:96px;height:96px;margin:0 auto 12px;border-radius:10px;background:linear-gradient(135deg,#e8e8ec,#f6d9d7)}
.service h3{position:absolute;left:641px;top:1812px;font-size:29px;font-weight:700;line-height:38px;color:var(--ink)}

/* testimonial */
.quote{position:absolute;left:346px;top:3030px;width:430px;font-size:17px;line-height:32px;font-style:italic;color:#555}

/* news */
.news-card{position:absolute;top:3572px;width:306px;height:392px;background:var(--white);box-shadow:0 4px 20px rgba(0,0,0,.08)}
.news-card .photo{position:absolute;left:6px;top:6px;width:294px;height:196px}
.tag{position:absolute;left:14px;top:218px;height:28px;padding:0 8px;font-size:15px;color:var(--white);display:flex;align-items:center}
.news-card h4{position:absolute;left:14px;top:264px;width:270px;font-size:21px;line-height:26px;color:var(--ink);font-weight:700}
.date{position:absolute;left:14px;top:355px;font-size:16px;color:#777;display:flex;gap:5px;align-items:center}

/* footer */
.footer{position:absolute;left:0;top:4155px;width:1200px;height:370px;background:var(--footer);color:var(--footer-text)}
.footer h5{font-size:18px;font-weight:700;color:var(--white);margin-bottom:14px}
.footer ul{list-style:none;font-size:16px;line-height:26px}
.social{position:absolute;top:4455px;width:42px;height:42px;border:2px solid #ddd;border-radius:50%}
</style>
</head>
<body>

<!-- Header & Hero -->
<section class="hero">
  <div class="logo" style="left:112px;top:28px">
    <span class="logo-dot"></span>
    <div>
      <div class="logo-name">taskharbor</div>
      <div class="logo-tag">your trusted advisor</div>
    </div>
  </div>
  <nav class="nav">
    <a class="active">Home</a><a>About</a><a>Services</a><a>Resources</a><a>Blog</a><a>Contact</a>
  </nav>
  <div class="phone">
    <svg width="16" height="16" viewBox="0 0 24 24"><path fill="#ec1f27" d="M6.6 10.8a15 15 0 0 0 6.6 6.6l2.2-2.2c.3-.3.7-.4 1-.2 1.1.4 2.3.6 3.6.6.6 0 1 .4 1 1V20c0 .6-.4 1-1 1A17 17 0 0 1 3 4c0-.6.4-1 1-1h3.5c.6 0 1 .4 1 1 0 1.3.2 2.5.6 3.6.1.3 0 .7-.2 1z"/></svg>
    1300 TH DESK
  </div>
  <h1>TaskHarbor</h1>
  <p class="lead">Your Trusted Advisor For Business Continuity Solutions</p>
  <a class="btn" style="left:112px;top:391px;width:184px;height:58px">Get More Info</a>
  <div class="placeholder" role="img" aria-label="Illustration of a computer monitor with business dashboards, charts, folders and a security shield"
       style="left:480px;top:115px;width:690px;height:470px;border-radius:20px;background:radial-gradient(circle at 55% 50%,#d6e4f2 0%,#e9eef4 55%,rgba(244,244,244,0) 75%)"></div>
</section>

<!-- Trusted by -->
<div class="card" style="left:110px;top:664px;width:980px;height:236px"></div>
<div class="trusted-title">Trusted by</div>
<div class="client" style="left:135px">Northlink</div>
<div class="client" style="left:325px">Veyra</div>
<div class="client active" style="left:515px">PlotBase</div>
<div class="client" style="left:706px">Kaminori</div>
<div class="client" style="left:896px">Stonefield</div>
<svg class="arrow" style="left:50px" viewBox="0 0 20 20"><path d="M13 2 5 10l8 8" fill="none" stroke="#555" stroke-width="2"/></svg>
<svg class="arrow" style="left:1122px" viewBox="0 0 20 20"><path d="M7 2l8 8-8 8" fill="none" stroke="#555" stroke-width="2"/></svg>

<!-- Welcome -->
<section class="welcome">
  <h2>Welcome to TaskHarbor</h2>
  <p class="body-copy abs" style="left:110px;top:1034px;width:430px">TaskHarbor Is Your Trusted Advisor For Business Continuity Solutions</p>
  <p class="body-copy abs" style="left:110px;top:1114px;width:430px">TaskHarbor's business continuity consultant's providing two core services:</p>
  <ul class="ticks abs" style="left:110px;top:1193px">
    <li><svg class="tick" viewBox="0 0 14 14"><path d="M2 7l3.5 3.5L12 3" fill="none" stroke="#d2453e" stroke-width="2.4"/></svg>Business Continuity Managed services</li>
    <li><svg class="tick" viewBox="0 0 14 14"><path d="M2 7l3.5 3.5L12 3" fill="none" stroke="#d2453e" stroke-width="2.4"/></svg>Business Continuity Consulting services</li>
  </ul>
  <a class="btn" style="left:110px;top:1282px;width:158px;height:58px">Read More</a>
  <div class="placeholder" role="img" aria-label="Video thumbnail: hands on a laptop showing financial charts"
       style="left:606px;top:977px;width:484px;height:299px;background:linear-gradient(135deg,#8e9aa8,#c9d2dc 55%,#e6eaee);box-shadow:0 6px 20px rgba(0,0,0,.12)"></div>
  <svg class="abs" style="left:818px;top:1097px" width="60" height="60" viewBox="0 0 60 60"><circle cx="30" cy="30" r="30" fill="#2a2a2a"/><path d="M24 19v22l18-11z" fill="#fff"/></svg>
</section>

<!-- What We Do -->
<div class="band" style="top:1414px;height:898px"></div>
<div class="section-title" style="top:1472px">What We Do</div>
<div class="card" style="left:110px;top:1564px;width:980px;height:664px"></div>
<div class="tab" style="left:129px"><div class="icon" role="img" aria-label="Resilience icon"></div>Resilience &amp;<br>Continuity</div>
<div class="tab" style="left:324px"><div class="icon" role="img" aria-label="Security icon"></div>Security<br>Management</div>
<div class="tab" style="left:518px"><div class="icon" role="img" aria-label="IT services icon"></div>IT Services &amp;<br>Solutions</div>
<div class="tab" style="left:714px"><div class="icon" role="img" aria-label="Data icon"></div>Data<br>Management</div>
<div class="tab" style="left:909px"><div class="icon" role="img" aria-label="Software icon"></div>Software<br>Solutions</div>
<div class="abs" style="left:134px;top:1770px;width:932px;height:3px;background:var(--line)"></div>
<div class="abs" style="left:156px;top:1769px;width:112px;height:4px;background:var(--accent)"></div>
<div class="placeholder" role="img" aria-label="Illustration of a businessman climbing steps towards a flag on a summit"
     style="left:162px;top:1820px;width:412px;height:326px;background:linear-gradient(160deg,#dfe4f3,#c6cfe8 60%,#eef0f8)"></div>
<section class="service">
  <h3>Resilience &amp;<br>Continuity Services</h3>
  <ul class="ticks abs" style="left:648px;top:1905px">
    <li><svg class="tick" viewBox="0 0 14 14"><path d="M2 7l3.5 3.5L12 3" fill="none" stroke="#d2453e" stroke-width="2.4"/></svg>Business Continuity Management</li>
    <li><svg class="tick" viewBox="0 0 14 14"><path d="M2 7l3.5 3.5L12 3" fill="none" stroke="#d2453e" stroke-width="2.4"/></svg>Disaster Recovery Planning</li>
    <li><svg class="tick" viewBox="0 0 14 14"><path d="M2 7l3.5 3.5L12 3" fill="none" stroke="#d2453e" stroke-width="2.4"/></svg>Crisis Management</li>
    <li><svg class="tick" viewBox="0 0 14 14"><path d="M2 7l3.5 3.5L12 3" fill="none" stroke="#d2453e" stroke-width="2.4"/></svg>Emergency Management Planning</li>
    <li><svg class="tick" viewBox="0 0 14 14"><path d="M2 7l3.5 3.5L12 3" fill="none" stroke="#d2453e" stroke-width="2.4"/></svg>Workplace Health and Safety</li>
    <li><svg class="tick" viewBox="0 0 14 14"><path d="M2 7l3.5 3.5L12 3" fill="none" stroke="#d2453e" stroke-width="2.4"/></svg>Pandemic Response Planning</li>
    <li><svg class="tick" viewBox="0 0 14 14"><path d="M2 7l3.5 3.5L12 3" fill="none" stroke="#d2453e" stroke-width="2.4"/></svg>Risk Management</li>
  </ul>
  <a class="btn" style="left:649px;top:2125px;width:158px;height:60px">Read More</a>
</section>

<!-- How to ensure -->
<section class="ensure">
  <h2 class="abs" style="left:108px;top:2378px;font-size:44px;line-height:49px">How To Ensure Your<br>Business Is 100% Safe</h2>
  <p class="body-copy abs" style="left:112px;top:2500px;width:490px">As an executive in any business, it is understandable that you want to ensure it is 100% safe, because your business is only as strong as its weakest link.</p>
  <p class="body-copy abs" style="left:112px;top:2606px;width:490px">You know that if you have a disastrous incident it will cause irreversible damage to your company's good name, your shareholders, board of directors and industry regulators. It will also cause severe legal ramifications.</p>
  <a class="btn" style="left:112px;top:2746px;width:158px;height:58px">Read More</a>
  <div class="placeholder" role="img" aria-label="Illustration of a document protected by a shield with a check mark"
       style="left:740px;top:2428px;width:320px;height:340px;border-radius:40px;background:radial-gradient(circle at 60% 55%,#dde6ee 0%,#e9eef3 50%,rgba(255,255,255,0) 78%)"></div>
</section>

<!-- Testimonials -->
<div class="band" style="top:2890px;height:527px;background:#f7f7f7"></div>
<div class="abs" style="left:789px;top:2890px;width:411px;height:527px;background:var(--accent)"></div>
<h2 class="abs" style="left:858px;top:2950px;font-size:40px;line-height:49px;color:var(--white)">Client<br>Testimonials</h2>
<svg class="abs" style="left:858px;top:3100px" width="212" height="180" viewBox="0 0 212 180">
  <path d="M0 180V90C0 40 25 8 80 0v36C50 42 42 60 42 80h50v100zM120 180V90c0-50 25-82 80-90v36c-30 6-38 24-38 44h50v100z" fill="#e07771"/>
</svg>
<div class="card" style="left:110px;top:2982px;width:710px;height:342px;border-radius:8px"></div>
<div class="abs" role="img" aria-label="Wavecomm client mark" style="left:152px;top:3022px;width:160px;height:160px;border-radius:50%;background:#f35a2c"></div>
<p class="quote">"With all due respect, I don't see TaskHarbor in the classic consultant mould. I see you far more as 'hands-on implementation practitioners', working closely with us to define and implement real solutions to meet our business strategies"</p>
<div class="abs" style="left:346px;top:3208px;font-size:19px;font-weight:700;color:#333">Daniel Ortner,</div>
<div class="abs" style="left:346px;top:3238px;font-size:15.5px;line-height:26px;color:#555">Head of Delivery Management –<br>Infrastructure Services, Wavecomm</div>
<svg class="abs" style="left:720px;top:3243px" width="60" height="24" viewBox="0 0 60 24">
  <circle cx="12" cy="12" r="11" fill="#999"/><path d="M14 7l-5 5 5 5" fill="none" stroke="#fff" stroke-width="2"/>
  <circle cx="47" cy="12" r="11" fill="#999"/><path d="M45 7l5 5-5 5" fill="none" stroke="#fff" stroke-width="2"/>
</svg>

<!-- Latest News -->
<div class="section-title" style="top:3482px">Latest News</div>
<article class="news-card" style="left:110px">
  <div class="photo" role="img" aria-label="Photo of dark server racks" style="background:linear-gradient(135deg,#2a2a2a,#6b6b6b 60%,#bdbdbd)"></div>
  <span class="tag" style="background:#d99a6c">Disaster Recovery</span>
  <h4>Decommissioning is Part of Disaster Recovery Planning</h4>
  <div class="date"><svg width="14" height="14" viewBox="0 0 14 14"><rect x="1" y="2" width="12" height="11" fill="none" stroke="#d2453e" stroke-width="1.6"/><path d="M1 5h12" stroke="#d2453e" stroke-width="1.6"/></svg>3 May 2018</div>
</article>
<article class="news-card" style="left:445px">
  <div class="photo" role="img" aria-label="Photo of a hand writing a note about adapting to change" style="background:linear-gradient(135deg,#f2f2f2,#d9d9d9 55%,#4f7fa8)"></div>
  <span class="tag" style="background:#6aa7dd">Business Continuity</span>
  <h4>Adapt or Die –<br>A Darwinian Take on Business Continuity</h4>
  <div class="date"><svg width="14" height="14" viewBox="0 0 14 14"><rect x="1" y="2" width="12" height="11" fill="none" stroke="#d2453e" stroke-width="1.6"/><path d="M1 5h12" stroke="#d2453e" stroke-width="1.6"/></svg>3 May 2018</div>
</article>
<article class="news-card" style="left:778px">
  <div class="photo" role="img" aria-label="Photo of hands being washed under a tap" style="background:linear-gradient(135deg,#5c6a66,#a9b3ae 55%,#d7dcd9)"></div>
  <span class="tag" style="background:#8cc98a">Pandemic</span>
  <h4>COVID19 – Business Recovery Phase</h4>
  <div class="date"><svg width="14" height="14" viewBox="0 0 14 14"><rect x="1" y="2" width="12" height="11" fill="none" stroke="#d2453e" stroke-width="1.6"/><path d="M1 5h12" stroke="#d2453e" stroke-width="1.6"/></svg>3 May 2018</div>
</article>
<a class="btn" style="left:521px;top:4016px;width:158px;height:58px">View More</a>

<!-- Footer -->
<footer class="footer">
  <div class="logo" style="left:112px;top:100px">
    <span class="logo-dot"></span>
    <div>
      <div class="logo-name">taskharbor</div>
      <div class="logo-tag" style="color:#999">your trusted advisor</div>
    </div>
  </div>
  <div class="abs" style="left:457px;top:48px">
    <h5>Quick Links</h5>
    <ul><li>Home</li><li>About</li><li>Services</li><li>Resources</li><li>Blog</li><li>Contact</li></ul>
  </div>
  <div class="abs" style="left:647px;top:48px">
    <h5>Legal</h5>
    <ul><li>Privacy</li><li>Disclaimer</li><li>Copyright</li><li>Spam Policy</li><li>Sitemap</li></ul>
  </div>
  <div class="abs" style="left:816px;top:48px;width:270px">
    <h5>Contact Us</h5>
    <ul style="font-size:15.5px;line-height:22px">
      <li style="display:flex;gap:10px"><svg width="12" height="16" viewBox="0 0 12 16" style="flex:none;margin-top:3px"><path d="M6 0a6 6 0 0 0-6 6c0 4.5 6 10 6 10s6-5.5 6-10a6 6 0 0 0-6-6zm0 8.5A2.5 2.5 0 1 1 6 3.5a2.5 2.5 0 0 1 0 5z" fill="#d2453e"/></svg>Level 14, Harbour Point, 88 Quayline Road, Sydney NSW 2000 Australia</li>
      <li style="display:flex;gap:10px;margin-top:20px"><svg width="14" height="14" viewBox="0 0 24 24" style="flex:none;margin-top:4px"><path fill="#d2453e" d="M6.6 10.8a15 15 0 0 0 6.6 6.6l2.2-2.2c.3-.3.7-.4 1-.2 1.1.4 2.3.6 3.6.6.6 0 1 .4 1 1V20c0 .6-.4 1-1 1A17 17 0 0 1 3 4c0-.6.4-1 1-1h3.5c.6 0 1 .4 1 1 0 1.3.2 2.5.6 3.6.1.3 0 .7-.2 1z"/></svg>1300 TH DESK</li>
      <li style="display:flex;gap:10px;margin-top:20px"><svg width="14" height="12" viewBox="0 0 14 12" style="flex:none;margin-top:5px"><rect width="14" height="12" fill="#d2453e"/><path d="M0 0l7 6 7-6" fill="none" stroke="#2d2d2d" stroke-width="1.4"/></svg>info@taskharbor.com</li>
    </ul>
  </div>
  <div class="abs" style="left:112px;top:275px;width:976px;height:1px;background:#4a4a4a"></div>
  <div class="abs" style="left:112px;top:312px;font-size:16px">Copyright © 2021, TaskHarbor. All rights reserved.</div>
</footer>
<span class="social" role="img" aria-label="Social profile link" style="left:886px"></span>
<span class="social" role="img" aria-label="Social profile link" style="left:938px"></span>
<span class="social" role="img" aria-label="Social profile link" style="left:990px"></span>
<span class="social" role="img" aria-label="Social profile link" style="left:1044px"></span>

</body>
</html>
```